Wandkalender Prächtiges Moorhavel
Zielgruppe
Souvenir- und Geschenkartiekl aus Ratzeburg
Aufgabenstellung
· Gesucht wird eine Designvorlage für die Gestaltung eines Jahreswandkalenders mit Naturfotos aus der Inselstadt Ratzeburg.
· Es muss nur ein Titelblatt und ein Monatsblatt gestaltet werden, die restlichen 11 Monate würden wir adaptieren.
· Das Format des Kalenders beträgt 50 x 70 cm im Hochformat
· Das Monatslayout soll Bilder im Hoch- und im Querformat zulassen
· Als Anlage habe ich einen ersten Entwurf von uns gepackt, der mir aber zu unoriginell bzw. zu konventionell ist.
· Die Zielgruppe ist tendenziell die Generation 50+

```html
<!DOCTYPE html>
<html lang="de">
<head>
<meta charset="utf-8">
<title>Wandkalender Prächtiges Moorhavel – April</title>
<link rel="stylesheet" href="https://fonts.googleapis.com/css2?family=Jost:wght@400;500&family=Yellowtail&display=swap">
<style>
  :root {
    --backdrop: #e4e4e4;
    --paper: #ffffff;
    --leaf-green: #5b9a35;
    --week-green: #3f9a22;
    --ink: #222222;
    --muted: #d2d2d2;
    --caption: #ffffff;
    --photo-sky: #dfe2da;
    --photo-brick: #b9795a;
    --photo-lawn: #5f9a2e;
    --photo-lawn-deep: #4f8a26;
  }
  * { margin: 0; padding: 0; box-sizing: border-box; }
  html, body {
    width: 1200px; height: 900px; overflow: hidden;
    background: var(--backdrop);
    font-family: "Jost", sans-serif;
  }
  .calendar-page {
    position: absolute; left: 300px; top: 30px;
    width: 600px; height: 840px;
    background: var(--paper);
    box-shadow: 0 4px 18px rgba(0,0,0,0.18);
  }
  .month-photo {
    position: absolute; left: 42px; top: 43px;
    width: 517px; height: 619px;
    background: linear-gradient(180deg,
      var(--photo-sky) 0%,
      var(--photo-brick) 38%,
      var(--photo-lawn) 58%,
      var(--photo-lawn-deep) 100%);
  }
  .photo-caption {
    position: absolute; right: 59px; top: 620px;
    width: 120px; text-align: right;
    font-size: 8.5px; line-height: 1.5; font-weight: 500;
    color: var(--caption);
  }
  .month-banner {
    position: absolute; left: 42px; top: 691px;
    width: 164px; height: 67px;
  }
  .month-banner svg { position: absolute; inset: 0; }
  .month-name {
    position: absolute; left: 20px; top: 6px;
    font-family: "Yellowtail", cursive;
    font-size: 44px; line-height: 1;
    color: var(--paper);
  }
  .month-grid {
    position: absolute; left: 250px; top: 684px;
    display: grid;
    grid-template-columns: 45px repeat(7, 39px);
    grid-template-rows: 29px repeat(5, 17px);
    font-size: 9.5px; font-weight: 400; color: var(--ink);
    align-items: center;
  }
  .month-grid span { text-align: center; }
  .month-grid .head { align-self: start; line-height: 20px; }
  .month-grid .week { color: var(--week-green); text-align: left; padding-left: 8px; }
  .month-grid .next { color: var(--muted); }
</style>
</head>
<body>
  <main class="calendar-page">
    <div class="month-photo" role="img" aria-label="Foto: Fachwerkhaus mit rotem Ziegeldach hinter Holzzaun und alten Linden, davor Rasen mit gelben Osterglocken"></div>
    <p class="photo-caption">Das Organistenhaus von 1644 auf dem Domhof.</p>

    <div class="month-banner">
      <svg width="164" height="67" viewBox="0 0 164 67" aria-hidden="true">
        <polygon points="0,0 164,0 131,33.5 164,67 0,67" fill="var(--leaf-green)"/>
      </svg>
      <span class="month-name">April</span>
    </div>

    <div class="month-grid">
      <span class="head week">WO</span><span class="head">MO</span><span class="head">DI</span><span class="head">MI</span><span class="head">DO</span><span class="head">FR</span><span class="head">SA</span><span class="head">SO</span>
      <span class="week">12</span><span>01</span><span>02</span><span>03</span><span>04</span><span>05</span><span>06</span><span>07</span>
      <span class="week">13</span><span>08</span><span>09</span><span>10</span><span>11</span><span>12</span><span>13</span><span>14</span>
      <span class="week">14</span><span>15</span><span>16</span><span>17</span><span>18</span><span>19</span><span>20</span><span>21</span>
      <span class="week">15</span><span>22</span><span>23</span><span>24</span><span>25</span><span>26</span><span>27</span><span>28</span>
      <span class="week">16</span><span>29</span><span>30</span><span class="next">01</span><span class="next">02</span><span class="next">03</span><span class="next">04</span><span class="next">05</span>
    </div>
  </main>
</body>
</html>
```